Business Card Design

Our Pharmacy Opens late - the last to close in Brisbane
over 30 years since opened.
Open from 7am - 11pm every day.
Next to Corvale 7 Day Medical Centre
Parking in front of shop
Sit with a pharmacist for every script - the best advice every time.
Private consulting room.
We have the medication that you need.
Wide range Home Health Care products.

Looking for a card that my (young) staff feel happy to hand out to people they they meet.
Updates

Hello Many thanks for your submissions I just need to clarify the costings for this project as per my updated brief Please confirm then we can proceed Many thanks Gordon

Reason: due to the adjusted brief and query I have extended the deadline Many thanks for those that have submitted, I will choose the designer as soon as I understand the costings of the project, as per the message despatched today Regards gordon

Target Market(s)

men and women 30-70

Industry/Entity Type

Business

Contact Information for Business Card

Pelltons Pharmacy - Corvale
317 Baxwood Rd
Corvale 4279
Last to Close
Open 7am - 11pm

Font styles to use
Sans Serif

Requirements
Must have
• each batch of 250 will have the following staff names

Corinne Maltby, Senior Pharmacist
Talia Pronk, Pharmacist
Bo Wang, Pharmacist
Ilsabet Crowther, Pharmacist
Nadia Voss, Retail Manager
Lucy Trembath, Marketing Manager
Gordon Pelltons, Pharmacist Proprietor
Should not have
• Please advise if the cost of this job covers the 7 individualised business cards.

Each staff member needs their own card.

please advise

```html
<!DOCTYPE html>
<html lang="en">
<head>
<meta charset="utf-8">
<title>Pelltons Pharmacy – Staff Business Card</title>
<link rel="stylesheet" href="https://fonts.googleapis.com/css2?family=Archivo+Black&family=Open+Sans:wdth,wght@75,300&display=swap">
<style>
  :root {
    --backdrop: #dcd8d6;
    --violet: #4a2fb0;
    --violet-deep: #2b1e8c;
    --lime: #e8f21c;
    --lemon: #f4f760;
    --ink-blue: #1410d8;
    --pale-text: #e9e6f2;
    --heading-grey: #8c8f9a;
  }
  * { box-sizing: border-box; margin: 0; padding: 0; }
  html, body {
    width: 1200px; height: 900px; overflow: hidden;
    background: var(--backdrop);
  }
  .card {
    position: absolute; left: 150px; top: 193px;
    width: 900px; height: 514px; overflow: hidden;
    box-shadow: 0 10px 30px rgba(0,0,0,.18);
  }
  .card__photo {
    position: absolute; inset: 0;
    background:
      radial-gradient(ellipse 48% 62% at 60% 56%, var(--lemon) 0%, var(--lime) 55%, rgba(232,242,28,0) 75%),
      linear-gradient(100deg, var(--violet-deep) 0%, var(--violet) 28%, #7d6fd0 40%, var(--lime) 55%, var(--lime) 100%);
  }
  .card__plate {
    position: absolute; left: 250px; top: 40px; width: 560px; height: 470px;
    border-radius: 50%; border: 3px solid rgba(255,255,255,.35);
  }
  .brand {
    position: absolute; left: 36px; top: 26px;
    display: flex; align-items: center; gap: 10px;
  }
  .brand__mark {
    width: 34px; height: 34px; border-radius: 50%;
    background: var(--lime);
  }
  .brand__name {
    font: 18px/1 'Archivo Black', sans-serif; color: var(--lime);
    text-transform: uppercase; letter-spacing: 1px;
  }
  .info {
    position: absolute; left: 250px; top: 82px; width: 610px;
    font-family: 'Archivo Black', sans-serif; color: var(--ink-blue);
  }
  .info__heading {
    font-family: 'Open Sans', sans-serif; font-weight: 300; font-stretch: 75%;
    font-size: 38px; line-height: 1;
    letter-spacing: 4px; text-transform: uppercase; color: var(--heading-grey);
    border-bottom: 2px solid var(--ink-blue); padding-bottom: 4px; display: inline-block;
  }
  .info__heading--staff { margin-top: 14px; }
  .contact { list-style: none; margin-top: 10px; }
  .contact li {
    font-size: 17px; line-height: 1.25; letter-spacing: 3px; text-transform: uppercase;
    text-shadow: 0 0 1px #fff;
  }
  .staff { list-style: none; margin-top: 8px; margin-left: -110px; }
  .staff li {
    font-size: 21px; line-height: 1.22; text-transform: uppercase;
    text-shadow: -1px -1px 0 var(--pale-text), 1px 1px 0 var(--pale-text);
  }
</style>
</head>
<body>
  <article class="card">
    <div class="card__photo" role="img" aria-label="Close-up photograph of colourful pills and capsules in violet and lime tones"></div>
    <div class="card__plate"></div>

    <div class="brand">
      <span class="brand__mark"></span>
      <span class="brand__name">Pelltons Pharmacy</span>
    </div>

    <section class="info">
      <h2 class="info__heading">Contact Information</h2>
      <ul class="contact">
        <li>Pelltons Pharmacy - Corvale</li>
        <li>317 Baxwood Rd Corvale 4279</li>
        <li>Last to Close Open 7am - 11pm</li>
      </ul>

      <h2 class="info__heading info__heading--staff">Staff Names</h2>
      <ul class="staff">
        <li>Corinne Maltby, Senior Pharmacist</li>
        <li>Talia Pronk, Pharmacist</li>
        <li>Bo Wang, Pharmacist</li>
        <li>Ilsabet Crowther, Pharmacist</li>
        <li>Nadia Voss, Retail Manager</li>
        <li>Lucy Trembath, Marketing Manager</li>
        <li>Gordon Pelltons, Pharmacist Proprietor</li>
      </ul>
    </section>
  </article>
</body>
</html>
```